Brantley Water Taxi and Transport

Need to redesign our business cards to relay that we do freight logistics and water taxi service. We also work with gov. agencies doing environmental clean up, oil spill response, remote site construction and work with many of the air taxi and helicopter services on Kodiak Island. Out website is www.brantleywatertaxi-example.com to get a better idea of what we do.

Contact Information for Business Card

I have a previous business card but it just has the logo on the front, and a sunset picture on the back with the contact info. It does not relay what we do and what we can help with. I like a simple straight forward design over a busy one.

Colors
3176b5
0455a3
cfdfed

Requirements
Must have
• logo, email, website, phone number

```html
<!DOCTYPE html>
<html lang="en">
<head>
<meta charset="utf-8">
<title>Brantley Water Taxi &amp; Transport – Business Cards</title>
<link href="https://fonts.googleapis.com/css2?family=Open+Sans:wght@400;600;700&display=swap" rel="stylesheet">
<style>
  :root {
    --brand-blue: #0455a3;
    --mid-blue: #3176b5;
    --pale-blue: #cfdfed;
    --accent-orange: #f5a623;
    --text-grey: #555a60;
    --card-white: #ffffff;
    --backdrop: #e6e9ed;
  }
  * { box-sizing: border-box; margin: 0; padding: 0; }
  html, body { width: 1200px; height: 892px; overflow: hidden; }
  body {
    background: var(--backdrop);
    font-family: "Open Sans", Arial, sans-serif;
    position: relative;
  }
  .card {
    position: absolute;
    width: 700px;
    height: 400px;
    background: var(--card-white);
    box-shadow: 0 6px 20px rgba(0,0,0,.18);
  }
  .card--front { left: 70px; top: 36px; }
  .card--back { left: 430px; top: 456px; }

  /* front */
  .front__emblem {
    position: absolute;
    left: 230px; top: 70px;
    width: 240px; height: 130px;
    background: linear-gradient(180deg, #f5b02a 0%, #bfe0f5 35%, #6bb8e6 70%, #3a8fd0 100%);
    border-radius: 4px;
  }
  .front__name {
    position: absolute;
    left: 0; right: 0; top: 218px;
    text-align: center;
    color: var(--brand-blue);
    font-weight: 700;
    font-size: 30px;
    line-height: 1.15;
  }
  .front__web {
    position: absolute;
    left: 0; right: 0; bottom: 58px;
    text-align: center;
    color: var(--text-grey);
    font-size: 15px;
    letter-spacing: 4px;
  }

  /* back */
  .back__boat {
    position: absolute;
    right: 90px; top: 30px;
    width: 230px; height: 110px;
    background: linear-gradient(180deg, #e9ecef 0%, #aeb6bf 55%, #6f7b88 100%);
    border-radius: 4px;
  }
  .back__details {
    position: absolute;
    left: 52px; bottom: 44px;
  }
  .back__company {
    color: var(--brand-blue);
    font-weight: 700;
    font-size: 26px;
    line-height: 1.15;
    margin-bottom: 16px;
  }
  .back__person {
    color: var(--brand-blue);
    font-weight: 700;
    font-size: 20px;
    line-height: 1.1;
  }
  .back__role {
    color: var(--accent-orange);
    font-size: 16px;
    letter-spacing: .5px;
    margin-bottom: 10px;
  }
  .back__contact {
    list-style: none;
    color: var(--text-grey);
    font-size: 16px;
    line-height: 1.4;
  }
</style>
</head>
<body>
  <section class="card card--front" aria-label="Business card front">
    <div class="front__emblem" role="img" aria-label="Illustration of a water taxi boat before snowy mountains under a rising sun"></div>
    <h1 class="front__name">Brantley<br>Water Taxi &amp; Transport</h1>
    <p class="front__web">www.brantleywatertaxi-example.com</p>
  </section>

  <section class="card card--back" aria-label="Business card back">
    <div class="back__boat" role="img" aria-label="Photograph of a grey water taxi vessel"></div>
    <div class="back__details">
      <h2 class="back__company">Brantley<br>Water Taxi &amp; Transport</h2>
      <p class="back__person">MILES CARVER</p>
      <p class="back__role">PRESIDENT</p>
      <ul class="back__contact">
        <li>(P) 555 0142 7788</li>
        <li>miles@brantleywatertaxi-example.com</li>
        <li>www.brantleywatertaxi-example.com</li>
      </ul>
    </div>
  </section>
</body>
</html>
```